New Business Card Design Project

Hi! We require a design for business cards for directors and head teachers of an international daycare for children 0 - 9. We are family-owned, -operated and -oriented. We have six locations, looking to franchise. Our USPs are: 1) Flexibility 2) Quality teachers 3) International culture 4) Best nutrition We are quality teachers and professional caretakers, but with creativity and personality! Business cards should be playful (but no Comic Sans or baby hand prints), colorful (but no rainbows), and have some breathing space. It should be obvious from the business card that we're a daycare. In 2020 we'll be launching our new website based on this design: https://plinvo.example/47K2RTWZMPD The font in the new website will be Houschka (medium, demibold, bold). We will keep our current logo, included in the files here. There are also screenshots of some designs we like. Show us your best! :)

Industry/Entity Type

Childcare

Contact Information for Business Card

Femke de Lorre
Communications Wizard
Pluma Tots International Daycare
Voskuilstraat 47 B, 2345 KR Leiden
www.plumatots.example
+31 647153826

Font styles to use
Serif
Sans Serif

Colors

Designer to choose colors to be used in the design.

Requirements
Must have
• Color

```html
<!DOCTYPE html>
<html lang="en">
<head>
<meta charset="utf-8">
<title>Pluma Tots – Business Card</title>
<link rel="stylesheet" href="https://fonts.googleapis.com/css2?family=Lato:wght@400;700;900&display=swap">
<style>
  :root {
    --bg: #e9e9eb;
    --card: #ffffff;
    --blue: #1a9bd0;
    --blue-dark: #1583b3;
    --pink: #e8457f;
    --ink: #1e1e1e;
    --dot-yellow: #f6ecc0;
    --dot-green: #e6efcf;
  }
  * { box-sizing: border-box; margin: 0; padding: 0; }
  html, body { width: 1200px; height: 900px; overflow: hidden; }
  body {
    background: var(--bg);
    font-family: "Lato", sans-serif;
    display: flex;
    flex-direction: column;
    align-items: center;
    justify-content: center;
    gap: 40px;
  }
  .card {
    width: 680px;
    height: 390px;
    border-radius: 22px;
    background: var(--card);
    box-shadow: 0 10px 30px rgba(0,0,0,.12);
    position: relative;
    overflow: hidden;
  }

  /* Back side */
  .card--back .pattern {
    position: absolute; inset: 0;
    background:
      radial-gradient(circle at 20% 30%, var(--dot-yellow) 0, transparent 45%),
      radial-gradient(circle at 80% 70%, var(--dot-green) 0, transparent 45%),
      linear-gradient(135deg, #faf4da 0%, #f3f6e6 100%);
  }
  .card--back .content {
    position: relative;
    height: 100%;
    display: flex;
    flex-direction: column;
    align-items: center;
    justify-content: center;
    gap: 42px;
  }
  .brand {
    display: flex;
    align-items: center;
    gap: 12px;
  }
  .brand__dot {
    width: 26px; height: 26px; border-radius: 50%;
    background: var(--blue);
  }
  .brand__name {
    font-weight: 900;
    color: var(--pink);
    font-size: 54px;
    letter-spacing: 1px;
  }
  .usps {
    text-align: center;
    color: var(--blue);
    font-size: 21px;
    line-height: 1.45;
  }
  .usps .num { color: var(--pink); }

  /* Front side */
  .card--front {
    display: flex;
    align-items: center;
    padding: 0 48px 0 50px;
  }
  .card--front .brand { width: 250px; justify-content: center; }
  .card--front .brand__name { font-size: 42px; }
  .divider {
    width: 3px;
    height: 190px;
    background: var(--blue);
    margin: 0 34px 0 26px;
    border-radius: 2px;
  }
  .details { flex: 1; }
  .details__name {
    color: var(--blue-dark);
    font-weight: 900;
    font-size: 30px;
    line-height: 1.1;
  }
  .details__role {
    color: var(--ink);
    font-size: 20px;
    margin-top: 4px;
  }
  .details__org {
    color: var(--blue);
    font-size: 19px;
    line-height: 1.35;
    margin-top: 22px;
  }
  .contact { margin-top: 20px; list-style: none; }
  .contact li {
    display: flex; align-items: center; gap: 10px;
    color: var(--ink);
    font-size: 20px;
    line-height: 1.4;
  }
  .contact svg { width: 20px; height: 20px; flex: none; }
</style>
</head>
<body>

  <section class="card card--back" aria-label="Card back">
    <div class="pattern" role="img" aria-label="Soft pastel yellow and green polka dot pattern"></div>
    <div class="content">
      <div class="brand">
        <span class="brand__dot"></span>
        <span class="brand__name">Pluma Tots</span>
      </div>
      <p class="usps">
        <span class="num">1)</span> Flexibility &nbsp; <span class="num">2)</span> Quality teachers<br>
        <span class="num">3)</span> International culture and <span class="num">4)</span> Best nutrition
      </p>
    </div>
  </section>

  <section class="card card--front" aria-label="Card front">
    <div class="brand">
      <span class="brand__dot"></span>
      <span class="brand__name">Pluma Tots</span>
    </div>
    <div class="divider"></div>
    <div class="details">
      <h1 class="details__name">Femke de Lorre</h1>
      <p class="details__role">Communications Wizard</p>
      <p class="details__org">Pluma Tots International Daycare<br>Voskuilstraat 47 B, 2345 KR Leiden</p>
      <ul class="contact">
        <li>
          <svg viewBox="0 0 20 20" aria-hidden="true"><circle cx="10" cy="10" r="10" fill="#1a9bd0"/><path d="M7 5.5c.4-.3 1-.2 1.2.2l.8 1.5c.2.4.1.8-.2 1.1l-.6.5c.5 1.1 1.3 2 2.4 2.5l.5-.6c.3-.3.8-.4 1.1-.2l1.5.8c.4.2.5.8.2 1.2l-.6.8c-.4.5-1.1.7-1.7.4C9.3 12.5 7.5 10.7 6.3 8.4c-.3-.6-.1-1.3.3-1.7z" fill="#fff"/></svg>
          +31 647153826
        </li>
        <li>
          <svg viewBox="0 0 20 20" aria-hidden="true"><circle cx="10" cy="10" r="10" fill="#1a9bd0"/><g fill="none" stroke="#fff" stroke-width="1.1"><circle cx="10" cy="10" r="5.5"/><ellipse cx="10" cy="10" rx="2.4" ry="5.5"/><path d="M4.5 10h11M5.3 7.3h9.4M5.3 12.7h9.4"/></g></svg>
          www.plumatots.example
        </li>
      </ul>
    </div>
  </section>

</body>
</html>
```